Niche Fitness Rebrand : Q7 Peak Conditioning

We're re-branding our fitness business and need to develop a cleaner, more sophisticated, and sleek website for our clients and potential clients to reference. We're looking to have some photo presence on all pages, with clean, crisp sections for easy reading on the web, and on mobile. We love the BVRdal(.com) website, which represents a very similar target market, and one of the same methods that our business represents. We're looking to take this local studio to a more professional level for future expansion, and need it to be sleek and in line with the growing and competitive marketplace for fitness.
Target Market(s)
70/30 women to men, physically active, upper middle class / professional between the ages of 28-42.
Industry/Entity Type
Fitness
Requirements
Must have
- sleek, professional, high-end design, with easy user navigation.
- About Page - with drop down child pages for management and coaches bios
- Classes Page 'The Methods' - with drop down child pages for different class types
- Location / Schedule Page
- Pricing
- Blog
- Private staff only programming login page
Nice to have
- potential to add an online retail shop -- but not currently necessary.
- Industry websites we like:
- www.bvrdal.example
- www.tarnbrookathletics.example

```html
<!DOCTYPE html>
<html lang="en">
<head>
<meta charset="utf-8">
<title>Q7 Peak Conditioning</title>
<link href="https://fonts.googleapis.com/css2?family=Montserrat:wght@600;700&family=Oswald:wght@500&family=Open+Sans:wght@400;600&display=swap" rel="stylesheet">
<style>
:root{
  --frame:#e6e6e6;
  --page:#ffffff;
  --ink:#1c1c1c;
  --gold:#b59c72;
  --body:#3d3d3d;
  --rule:#cfcfcf;
  --bar:#111111;
}
*{box-sizing:border-box;margin:0;padding:0}
html,body{width:1151px;height:1200px;overflow:hidden;background:var(--frame)}
.page{position:absolute;left:13px;top:13px;width:1125px;height:1173px;background:var(--page)}
.topbar{position:absolute;left:629px;top:0;width:473px;height:36px}
.topbar-shape{position:absolute;left:0;top:0}
.info{position:absolute;left:54px;top:0;height:36px;display:flex;align-items:center;gap:8px;color:#fff;font:700 14px "Montserrat",sans-serif;white-space:nowrap}
.info svg{flex:none;display:block}
.social{position:absolute;left:350px;top:7px;display:flex;gap:4px}
.social span{width:22px;height:22px;border:1.5px solid #fff;border-radius:50%}
.brand{position:absolute;left:23px;top:24px;display:flex;align-items:center;gap:12px}
.brand-mark{flex:none;width:80px;height:80px;border:6px solid var(--ink)}
.brand-name{font:700 27px/1.05 "Montserrat",sans-serif;color:var(--ink);letter-spacing:.5px;white-space:nowrap}
.nav{position:absolute;left:624px;top:88px;display:flex;gap:18px;font:500 16px "Oswald",sans-serif;color:var(--ink);text-transform:uppercase}
.nav a{color:inherit;text-decoration:none;padding-bottom:3px}
.nav a.current{border-bottom:4px solid var(--gold)}
.hero{position:absolute;left:0;top:124px;width:1125px;height:531px;background:linear-gradient(90deg,#2b2018 0%,#5a4232 30%,#8a6a4f 55%,#c9ab85 80%,#a3876a 100%)}
.hero-shadow{position:absolute;left:35px;top:655px;width:1055px;height:14px;background:radial-gradient(ellipse at top,rgba(0,0,0,.22),rgba(0,0,0,0) 70%)}
.about-title{position:absolute;left:0;top:712px;width:1125px;display:flex;justify-content:center;align-items:center;gap:22px;font:700 24px "Montserrat",sans-serif;color:#2c2c2c;white-space:nowrap}
.about-title::before,.about-title::after{content:"";width:88px;height:1px;background:var(--rule)}
.about-title em{font-style:normal;color:var(--gold)}
.about-copy{position:absolute;left:68px;top:781px;width:990px;text-align:center;font:400 12.2px/19px "Open Sans",sans-serif;color:var(--body)}
.footer{position:absolute;left:0;top:1022px;width:1125px;height:115px;background:linear-gradient(#fff 0%,#f0f0f0 40%,#d4d4d4 100%)}
.footer-brand{position:absolute;left:434px;top:956px;display:flex;align-items:center;gap:12px}
.footer-nav{position:absolute;left:0;top:1089px;width:1125px;display:flex;justify-content:center;gap:22px;font:600 13.5px "Montserrat",sans-serif;letter-spacing:1px;color:#333}
.copyright{position:absolute;left:0;top:1147px;width:1125px;text-align:center;font:600 11px "Open Sans",sans-serif;color:#333}
</style>
</head>
<body>
<div class="page">
  <div class="topbar">
    <svg class="topbar-shape" width="473" height="36" viewBox="0 0 473 36"><polygon points="0,0 473,0 439,36 34,36" fill="var(--bar)"/></svg>
    <div class="info">
      <svg width="22" height="22" viewBox="0 0 22 22"><circle cx="11" cy="11" r="10" fill="none" stroke="#fff" stroke-width="1.5"/><path d="M7.5 6.5l2 -.5 1 2.5-1.3 1a6 6 0 0 0 2.8 2.8l1-1.3 2.5 1-.5 2c-4 .3-7.8-3.5-7.5-7.5z" fill="#fff"/></svg>
      <span>FOR INFORMATION : 555-010-4477</span>
    </div>
    <div class="social"><span></span><span></span><span></span></div>
  </div>

  <div class="brand">
    <div class="brand-mark"></div>
    <div class="brand-name">Q7 PEAK<br>CONDITIONING</div>
  </div>

  <nav class="nav">
    <a class="current" href="#">Home</a><a href="#">About</a><a href="#">Classes</a><a href="#">Location</a><a href="#">Pricing</a><a href="#">Blog</a><a href="#">Contact</a>
  </nav>

  <div class="hero" role="img" aria-label="Photo of a fit athlete's torso holding a dumbbell against a warm textured wall"></div>
  <div class="hero-shadow"></div>

  <h2 class="about-title"><span>ABOUT <em>Q7 PEAK CONDITIONING</em></span></h2>
  <p class="about-copy">Lorem ipsum dolor sit amet, consectetuer adipiscing elit, sed diam nonummy nibh euismod tincidunt ut laoreet dolore magna aliquam erat volutpat. Ut wisi enim ad minim veniam, quis nostrud exerci tation ullamcorper suscipit lobortis nisl ut aliquip ex ea commodo consequat. Duis autem vel eum iriure dolor in hendrerit in vulputate velit esse molestie consequat, vel illum dolore eu feugiat nulla facilisis at vero eros et accumsan et iusto odio dignissim qui blandit praesent luptatum zzril delenit augue duis dolore te feugait nulla facilisi. Nam liber tempor cum soluta nobis eleifend option congue nihil imperdiet doming id quod mazim placerat facer possim assum. Typi non habent claritatem insitam; est usus legentis in iis qui facit eorum claritatem. Investigationes demonstraverunt lectores legere me lius quod ii legunt saepius.</p>

  <div class="footer"></div>
  <div class="footer-brand">
    <div class="brand-mark"></div>
    <div class="brand-name">Q7 PEAK<br>CONDITIONING</div>
  </div>
  <nav class="footer-nav"><span>Home</span><span>About</span><span>Classes</span><span>Location</span><span>Pricing</span><span>Blog</span><span>Contact</span></nav>
  <p class="copyright">© 2017 Q7 PEAK CONDITIONING I ALL RIGHTS RESERVED</p>
</div>
</body>
</html>
```